Accountant services flyer & marketing portfolio

I require a design for a marketing portfolio of blank templates for a flyer, product brochure, report cover for A4 based on our style - current logo, letterhead, website look and feel - that can be updated in publisher or word with relevant marketing and company information editorial material and text. It will be either printed A4 or saved as PDF and distributed

Target Market(s)

small business and investment / superfund clients

Industry/Entity Type

Accountant

Font styles to use
Sans Serif

Requirements
Must have
• Instyle of letterhead and website
Professional body logos
Space to input text
Relevant happy images
Nice to have
• Images of happy lifestyle types retirees, young families and mid-aged
tradesmen and professionals

```html
<!DOCTYPE html>
<html lang="en">
<head>
<meta charset="utf-8">
<title>Solstice Advisory – Flyer</title>
<link rel="stylesheet" href="https://fonts.googleapis.com/css2?family=Open+Sans:wght@400;600;700&display=swap">
<style>
  :root {
    --bg: #8f8f8f;
    --paper: #ffffff;
    --orange-light: #f7a534;
    --orange: #f28c28;
    --orange-deep: #ee5a24;
    --ink: #1f1f1f;
    --body: #555555;
    --badge-panel: #f1f2f4;
  }
  * { margin: 0; padding: 0; box-sizing: border-box; }
  html, body { width: 1200px; height: 2493px; overflow: hidden; }
  body { background: var(--bg); font-family: "Open Sans", Arial, sans-serif; position: relative; }

  .flyer {
    position: absolute; left: 50px; top: 536px;
    width: 995px; height: 1287px;
    background: var(--paper);
    transform: scale(1.1055); transform-origin: top left;
    overflow: hidden;
  }
  .swoosh { position: absolute; left: 0; top: 0; }
  .photo { position: absolute; border-radius: 50%; border: 6px solid var(--paper); }
  .photo--seniors { left: 314px; top: 504px; width: 198px; height: 198px;
    background: radial-gradient(circle at 45% 40%, #e9dccd, #b9a58f 60%, #8f7c69); }
  .photo--couple { left: 482px; top: 280px; width: 384px; height: 384px;
    background: radial-gradient(circle at 50% 45%, #d9a27d, #8d6248 55%, #4e4040); }

  .hero { position: absolute; left: 67px; top: 76px; color: #fff; }
  .hero__title { font-size: 44px; font-weight: 700; line-height: 46px; letter-spacing: -0.3px; white-space: nowrap; }
  .hero__rule { display: flex; gap: 6px; margin: 8px 0 26px; }
  .hero__rule span { height: 3px; background: #fff; }
  .hero__text { width: 368px; font-size: 14.5px; font-weight: 600; line-height: 23px; text-align: justify; margin-bottom: 22px; }
  .hero__text--short { width: 330px; text-align: left; }

  .brand { position: absolute; left: 620px; top: 96px; width: 340px; text-align: center; }
  .brand__mark { width: 46px; height: 46px; border-radius: 50%; background: var(--orange-deep); margin: 0 auto 22px; }
  .brand__name { color: var(--ink); font-size: 27px; font-weight: 600; line-height: 32px; }
  .brand__tagline { color: var(--ink); font-size: 19px; line-height: 24px; }

  .column { position: absolute; top: 702px; color: var(--body); font-size: 14px; line-height: 23px; }
  .column--left { left: 67px; width: 468px; }
  .column--right { left: 577px; width: 355px; text-align: justify; }
  .column h2 { color: var(--ink); font-size: 27px; font-weight: 600; line-height: 37px; margin-bottom: 16px; }
  .column p + p { margin-top: 22px; }

  .list { position: absolute; top: 980px; width: 275px; color: var(--body); font-size: 14px; line-height: 23px; }
  .list--one { left: 67px; }
  .list--two { left: 362px; }
  .list h3 { color: var(--orange-deep); font-size: 27px; font-weight: 600; line-height: 34px; margin-bottom: 14px; }
  .list ul { list-style: none; }
  .list li { position: relative; padding-left: 12px; margin-bottom: 8px; }
  .list li::before { content: ""; position: absolute; left: 1px; top: 10px; width: 5px; height: 5px; border-radius: 50%; background: var(--orange-deep); }

  .partners { position: absolute; left: 653px; top: 1035px; width: 252px; height: 160px; background: var(--badge-panel); }
  .partner { position: absolute; }

  .footer { position: absolute; left: 0; top: 1200px; width: 995px; height: 87px;
    background: linear-gradient(90deg, var(--orange-light), var(--orange-deep)); color: #fff; font-size: 16.5px; line-height: 25px; }
  .footer__item { position: absolute; top: 20px; display: flex; gap: 8px; }
  .footer__item svg { flex: none; margin-top: 6px; }
</style>
</head>
<body>
  <main class="flyer">
    <svg class="swoosh" width="995" height="700" viewBox="0 0 995 700" aria-hidden="true">
      <defs>
        <linearGradient id="heroGrad" x1="0" y1="0" x2="1" y2="1">
          <stop offset="0" stop-color="#f39a2a"/>
          <stop offset="0.6" stop-color="#f07a28"/>
          <stop offset="1" stop-color="#ee5a24"/>
        </linearGradient>
      </defs>
      <path d="M0,0 H612 C645,230 560,490 330,605 C220,652 100,666 0,670 Z" fill="var(--orange-light)"/>
      <path d="M0,0 H445 C565,80 585,270 500,410 C420,540 250,615 0,640 Z" fill="url(#heroGrad)"/>
    </svg>

    <div class="photo photo--seniors" role="img" aria-label="Photo of a smiling retired couple looking at a tablet"></div>
    <div class="photo photo--couple" role="img" aria-label="Photo of a happy young couple lying on a picnic blanket"></div>

    <section class="hero">
      <h1 class="hero__title">It has<br>survived not only<br>five centuries</h1>
      <div class="hero__rule"><span style="width:62px"></span><span style="width:28px"></span></div>
      <p class="hero__text">Lorem Ipsum is simply dummy text of the printing and typesetting industry. Lorem Ipsum has been the industry's standard dummy text ever since the 1500s, when an unknown printer took.</p>
      <p class="hero__text hero__text--short">Galley of type and scrambled it to make a type specimen book. It has survived not only five centuries</p>
    </section>

    <header class="brand">
      <div class="brand__mark"></div>
      <div class="brand__name">Solstice Advisory</div>
      <div class="brand__tagline">Clear advice. Steady growth</div>
    </header>

    <article class="column column--left">
      <h2>Lorem Ipsum is<br>simply dummy text of the</h2>
      <p>Lorem Ipsum is simply dummy text of the printing and typesetting industry. Lorem Ipsum has been the industry's standard dummy text ever since the 1500s, when an unknown printer took a galley of type and scrambled it to make a type specimen book.</p>
      <p>It has survived not only five centuries, but also the leap into electronic typesetting, remaining essentially unchanged.</p>
    </article>

    <article class="column column--right">
      <h2>Lorem Ipsum is<br>simply dummy text of the</h2>
      <p>Lorem Ipsum is simply dummy text of the printing and typesetting industry. Lorem Ipsum has been the industry's standard dummy Text ever since the 1500s, when an unknown</p>
      <p>It has survived not only five centuries, but also the leap into electronic typesetting, remaining essentially unchanged</p>
    </article>

    <section class="list list--one">
      <h3>Lorem Ipsum</h3>
      <ul>
        <li>Lorem Ipsum is simply dummy text of the printing and typesetting.</li>
        <li>Lorem Ipsum has been the industry's</li>
        <li>Standard dummy text ever since the the printing and typesetting.</li>
      </ul>
    </section>

    <section class="list list--two">
      <h3>Lorem Ipsum</h3>
      <ul>
        <li>Lorem Ipsum is simply dummy text of the printing and typesetting.</li>
        <li>Lorem Ipsum has been the industry's</li>
        <li>Standard dummy text ever since the the printing and typesetting.</li>
      </ul>
    </section>

    <aside class="partners" aria-label="Professional body memberships">
      <div class="partner" style="left:22px;top:32px;width:72px;height:32px;background:#1f3a8a"></div>
      <div class="partner" style="left:108px;top:16px;width:42px;height:50px;background:#111"></div>
      <div class="partner" style="left:168px;top:38px;width:62px;height:18px;background:#bdbdbd"></div>
      <div class="partner" style="left:36px;top:100px;width:28px;height:28px;border-radius:50%;background:#c9cdd6"></div>
      <div class="partner" style="left:100px;top:102px;width:56px;height:24px;background:#a9a1c9"></div>
      <div class="partner" style="left:178px;top:100px;width:28px;height:28px;border-radius:50%;background:#3bb8b0"></div>
      <div class="partner" style="left:208px;top:100px;width:28px;height:28px;border-radius:50%;background:#2aa79e"></div>
    </aside>

    <footer class="footer">
      <div class="footer__item" style="left:67px">
        <svg width="14" height="14" viewBox="0 0 14 14" aria-hidden="true"><circle cx="7" cy="7" r="7" fill="#fff"/><path d="M4.5,3.5 l1.5,1.5 -1,1 c.7,1.3 1.5,2.1 2.8,2.8 l1-1 1.7,1.5 -1,1.4 c-2.8,-.3 -5.4,-2.9 -5.8,-5.8z" fill="var(--orange-deep)"/></svg>
        <div>1300 000 123<br>612 4000 5120</div>
      </div>
      <div class="footer__item" style="left:270px;top:14px">
        <svg width="14" height="14" viewBox="0 0 14 14" aria-hidden="true"><circle cx="7" cy="7" r="7" fill="#fff"/><rect x="3.5" y="4.5" width="7" height="5" fill="none" stroke="var(--orange)" stroke-width="1"/><path d="M3.5,4.5 l3.5,3 3.5,-3" fill="none" stroke="var(--orange)" stroke-width="1"/></svg>
        <div>mail@solsticeadvisory.example<br>www.solsticeadvisory.example</div>
      </div>
      <div class="footer__item" style="left:593px;top:16px">
        <svg width="12" height="16" viewBox="0 0 12 16" aria-hidden="true"><path d="M6,0 C2.7,0 0,2.6 0,5.8 0,10 6,16 6,16 6,16 12,10 12,5.8 12,2.6 9.3,0 6,0z" fill="#fff"/><circle cx="6" cy="6" r="2.2" fill="var(--orange-deep)"/></svg>
        <div>Suite 12, Level 2, 48 Harbour Road<br>Seaview NSW 2999</div>
      </div>
    </footer>
  </main>
</body>
</html>
```